Business Card Design for Law firm - already have logo

Now that we have a logo, we need a business card design - our logo is attached -it is salaryman font if that helps - we would like a file that can be uploaded to kellumo (www.kellumo.com) using the logo and with the following information on it:
Dunmore Law Firm, P.C.
Felix Dunmore, Esq.
6718 NE 19th Ave.
Portland, OR 97284
971.555.0142 phone
971.555.0187 fax
fel@dunmore.net
Voxly: feldunmore
Chatline: felix.dunmore@quillmail.com
Target Market(s)
our business cards are distributed to corporate executives, technology professionals and healthcare providers
Industry/Entity Type
Business
Look and feel

```html
<!DOCTYPE html>
<html lang="en">
<head>
<meta charset="utf-8">
<title>Dunmore Law Firm, P.C. — Business Card</title>
<link rel="stylesheet" href="https://fonts.googleapis.com/css2?family=Tinos&display=swap">
<style>
  :root {
    --backdrop: #000000;
    --card: #ffffff;
    --ink: #111111;
    --accent: #e8141b;
  }
  html, body {
    margin: 0;
    padding: 0;
    width: 1200px;
    height: 800px;
    overflow: hidden;
    background: var(--backdrop);
  }
  .canvas {
    position: relative;
    width: 1200px;
    height: 800px;
    background: var(--backdrop);
    font-family: "Tinos", "Times New Roman", serif;
    color: var(--ink);
  }
  .card {
    position: absolute;
    left: 57px;
    top: 57px;
    width: 1068px;
    height: 690px;
    background: var(--card);
  }
  .brand {
    position: absolute;
    left: 50px;
    top: 50px;
    margin: 0;
    font-size: 86px;
    line-height: 118px;
    letter-spacing: 8px;
    font-weight: 400;
    color: var(--ink);
  }
  .identity {
    position: absolute;
    left: 0;
    right: 0;
    top: 272px;
    text-align: center;
  }
  .identity__name {
    margin: 0 0 0 106px;
    font-size: 50px;
    line-height: 54px;
    font-weight: 400;
    color: var(--accent);
  }
  .identity__address {
    margin: 0 0 0 106px;
    font-style: normal;
    font-size: 24px;
    line-height: 28px;
  }
  .contact-online {
    position: absolute;
    left: 43px;
    top: 538px;
    margin: 0;
    font-size: 26px;
    line-height: 34px;
  }
  .contact-online .email { display: block; color: var(--ink); margin-bottom: 6px; }
  .contact-online .im { display: block; color: var(--accent); line-height: 34px; }
  .contact-phone {
    position: absolute;
    left: 720px;
    width: 290px;
    top: 534px;
    margin: 0;
    text-align: center;
    font-size: 25px;
    line-height: 32px;
  }
  .contact-phone span { display: block; }
</style>
</head>
<body>
<main class="canvas">
  <section class="card">
    <p class="brand">DUNMORE</p>

    <div class="identity">
      <h1 class="identity__name">FELIX DUNMORE, ESQ.</h1>
      <address class="identity__address">
        DUNMORE LAW FIRM, P.C.<br>
        6718 NE 19TH AVE.<br>
        PORTLAND, OR 97284
      </address>
    </div>

    <p class="contact-online">
      <span class="email">FEL@DUNMORE.NET</span>
      <span class="im">VOXLY: FELDUNMORE</span>
      <span class="im">CHATLINE: FELIX.DUNMORE@QUILLMAIL.COM</span>
    </p>

    <p class="contact-phone">
      <span>971.555.0142 PHONE</span>
      <span>971.555.0187 FAX</span>
    </p>
  </section>
</main>
</body>
</html>
```